Brennick Holdings Business Cards

These are professional business cards that are for my family office.
Put fake emails and phone numbers as of now until I finalize those components. This family office controls my families investments, assets, and future. The cards should be professional.
..
.
.
.
I just uploaded another variation of a logo I would like to see as a business card to I am inbeteen which logo to use

Target Market(s)

business

Industry/Entity Type

business

Contact Information for Business Card

Professional, wealth related, finance related.

Requirements
Must have
• Logo

```html
<!DOCTYPE html>
<html lang="en">
<head>
<meta charset="utf-8">
<title>Brennick Holdings Business Cards</title>
<link rel="stylesheet" href="https://fonts.googleapis.com/css2?family=Montserrat:wght@400;600&display=swap">
<style>
  :root {
    --stage: #d8d3cb;
    --card: #1b2130;
    --card-edge: #141926;
    --ink-white: #f3f4f7;
    --ink-soft: #dfe2e8;
    --ink-grey: #9ea3ad;
    --accent: #4a5ba8;
    --accent-deep: #2b3561;
    --silver: #8a90a0;
  }
  * { margin: 0; padding: 0; box-sizing: border-box; }
  html, body { width: 900px; height: 1200px; overflow: hidden; }
  body {
    background: var(--stage);
    font-family: "Montserrat", Arial, sans-serif;
    position: relative;
  }
  .card {
    position: absolute;
    background: linear-gradient(160deg, #1f2637 0%, var(--card) 55%, var(--card-edge) 100%);
    border-radius: 22px;
    overflow: hidden;
    box-shadow: 0 10px 24px rgba(0,0,0,.35);
  }
  .card--front { left: 80px; top: 130px; width: 742px; height: 442px; }
  .card--back  { left: 78px; top: 638px; width: 744px; height: 440px; }

  .wordmark {
    position: absolute; left: 37px; top: 74px;
    font-size: 27px; font-weight: 600; letter-spacing: 1.2px;
    text-transform: uppercase; color: var(--ink-white);
  }
  .emblem-field {
    position: absolute; left: 438px; top: 14px; width: 420px; height: 420px;
    border-radius: 50%;
    background: radial-gradient(circle at 62% 48%, #34407a 0%, var(--accent-deep) 38%, #1f2742 70%, #1a2031 100%);
    box-shadow: 0 0 0 1px rgba(74,91,168,.35);
  }
  .holder-name {
    position: absolute; left: 37px; top: 190px;
    font-size: 26px; font-weight: 600; color: var(--ink-grey);
  }
  .holder-role {
    position: absolute; left: 37px; top: 221px;
    font-size: 16px; color: var(--ink-soft);
  }
  .address {
    position: absolute; left: 38px; top: 270px;
    font-size: 16px; line-height: 21px; color: var(--ink-soft);
    font-style: normal;
  }
  .contact-list { position: absolute; left: 38px; top: 327px; list-style: none; }
  .contact-list li {
    display: flex; align-items: center; gap: 9px;
    height: 28px; font-size: 16px; color: var(--ink-soft);
  }
  .contact-list svg { width: 15px; height: 15px; fill: var(--ink-soft); flex: none; }

  .back-pattern {
    position: absolute; inset: 0;
    background:
      radial-gradient(ellipse at 0% 0%, rgba(160,166,182,.55) 0%, rgba(110,117,136,.35) 30%, rgba(27,33,48,0) 62%),
      linear-gradient(125deg, #3a4156 0%, #262d40 40%, #1b2130 70%, #181d2b 100%);
  }
  .back-brand {
    position: absolute; left: 240px; top: 290px; width: 332px;
    text-align: right;
    font-size: 20px; font-weight: 600; letter-spacing: 1px;
    text-transform: uppercase; color: var(--ink-white);
  }
  .back-mark {
    position: absolute; left: 586px; top: 268px; width: 74px; height: 74px;
    border: 2px solid var(--ink-white); border-radius: 50%;
  }
</style>
</head>
<body>
  <section class="card card--front">
    <div class="emblem-field" role="img" aria-label="Large faded brand emblem decoration"></div>
    <div class="wordmark">Brennick Holdings</div>
    <h1 class="holder-name">Marcus Ellery</h1>
    <p class="holder-role">Owner</p>
    <address class="address">42 Fairmount Court<br>Ridgeview, NJ 07011 USA</address>
    <ul class="contact-list">
      <li>
        <svg viewBox="0 0 24 24" aria-hidden="true"><path d="M6.6 10.8a15.1 15.1 0 0 0 6.6 6.6l2.2-2.2a1 1 0 0 1 1-.25 11.4 11.4 0 0 0 3.6.57 1 1 0 0 1 1 1V20a1 1 0 0 1-1 1A17 17 0 0 1 3 4a1 1 0 0 1 1-1h3.5a1 1 0 0 1 1 1c0 1.25.2 2.46.57 3.6a1 1 0 0 1-.25 1z"/></svg>
        (555)214-7830
      </li>
      <li>
        <svg viewBox="0 0 24 24" aria-hidden="true"><path d="M2 5h20v14H2z"/><path d="M2 6l10 7 10-7" fill="none" stroke="var(--card)" stroke-width="1.6"/></svg>
        info@yourwebsitename.com
      </li>
      <li>
        <svg viewBox="0 0 24 24" aria-hidden="true"><circle cx="12" cy="12" r="10"/><path d="M2 12h20M12 2c3 3 3 17 0 20M12 2c-3 3-3 17 0 20" fill="none" stroke="var(--card)" stroke-width="1.5"/></svg>
        www.yourwebsitename.com
      </li>
    </ul>
  </section>

  <section class="card card--back">
    <div class="back-pattern" role="img" aria-label="Repeated brand emblem pattern fading from silver to dark"></div>
    <div class="back-brand">Brennick Holdings</div>
    <div class="back-mark"></div>
  </section>
</body>
</html>
```